Lift Every Ledger Through Chairside Trust

Design a cover for this book which is designed to help a business go from it's current revenue and treatment acceptance to double (2X) that success and those metrics.

```html
<!DOCTYPE html>
<html lang="en">
<head>
<meta charset="utf-8">
<title>Lift Every Ledger Through Chairside Trust — Book Cover</title>
<link rel="stylesheet" href="https://fonts.googleapis.com/css2?family=Poppins:wght@600;700&family=Inter:wght@500&display=swap">
<style>
  :root {
    --backdrop: #c3c6cb;
    --cover-navy: #343f6c;
    --ink-white: #f6f5f0;
    --chart-blue: #2f8fd2;
    --chart-blue-deep: #2a6fb0;
    --rule-teal: #8cc4bd;
  }
  * { margin: 0; padding: 0; box-sizing: border-box; }
  html, body {
    width: 1200px;
    height: 796px;
    overflow: hidden;
    background: var(--backdrop);
  }
  .stage {
    position: relative;
    width: 1200px;
    height: 796px;
  }
  .book-cover {
    position: absolute;
    left: 400px;
    top: 109px;
    width: 407px;
    height: 577px;
    background: var(--cover-navy);
    color: var(--ink-white);
    overflow: hidden;
  }
  .author-name {
    position: absolute;
    top: 27px;
    left: 0;
    width: 100%;
    text-align: center;
    font-family: "Poppins", sans-serif;
    font-weight: 600;
    font-size: 17px;
    letter-spacing: 1.8px;
  }
  .title-lead {
    position: absolute;
    top: 129px;
    left: 0;
    width: 100%;
    text-align: center;
    font-family: "Poppins", sans-serif;
    font-weight: 700;
    font-size: 140px;
    line-height: 1;
    letter-spacing: -3px;
    white-space: nowrap;
  }
  .chart-art {
    position: absolute;
    left: 82px;
    top: 262px;
    width: 259px;
    height: 96px;
    background: linear-gradient(90deg, var(--chart-blue-deep), var(--chart-blue));
    opacity: 0.85;
  }
  .chart-baseline {
    position: absolute;
    left: 0;
    top: 358px;
    width: 100%;
    height: 3px;
    background: var(--rule-teal);
  }
  .title-main {
    position: absolute;
    top: 377px;
    left: 0;
    width: 100%;
    text-align: center;
    font-family: "Poppins", sans-serif;
    font-weight: 700;
    font-size: 52px;
    line-height: 53px;
  }
  .title-subline {
    position: absolute;
    top: 487px;
    left: 0;
    width: 100%;
    text-align: center;
    font-family: "Inter", sans-serif;
    font-weight: 500;
    font-size: 18px;
    line-height: 22px;
  }
</style>
</head>
<body>
<main class="stage">
  <section class="book-cover">
    <p class="author-name">OWEN HARTLEY</p>
    <h1 class="title-lead">LIFT</h1>
    <div class="chart-art" role="img" aria-label="Illustration of a rising bar chart with an upward trend arrow"></div>
    <div class="chart-baseline"></div>
    <h2 class="title-main">EVERY<br>LEDGER</h2>
    <p class="title-subline">THROUGH CHAIRSIDE<br>TRUST</p>
  </section>
</main>
</body>
</html>
```